PowerPoint Template

We would like new powerpoint template for our organization: Fjordvik Data Guild.
Enclosed you find our logo and old template.
Industry/Entity Type
Computer
Requirements
Must have
- 1. Logo
2. Footer (for autor)
3. Font: Variations of ARIAL

```html
<!DOCTYPE html>
<html lang="no">
<head>
<meta charset="utf-8">
<title>Fjordvik Data Guild – Presentation Template</title>
<link rel="stylesheet" href="https://fonts.googleapis.com/css2?family=Arimo:wght@400;700&family=Carlito&display=swap">
<style>
  :root {
    --board: #728486;
    --slide: #ffffff;
    --pink: #fcc0e0;
    --cyan: #c0f0f4;
    --mint: #c0f8dc;
    --stone: #e6eae8;
    --ink: #111111;
    --brand-red: #e8203a;
    --bullet-blue: #1a6fd6;
    --shadow: rgba(0, 0, 0, 0.55);
  }
  html, body {
    margin: 0;
    padding: 0;
    width: 1200px;
    height: 929px;
    overflow: hidden;
    background: var(--board);
  }
  .board {
    position: relative;
    width: 1200px;
    height: 929px;
  }
  .slide {
    position: absolute;
    background: var(--slide);
    overflow: hidden;
    box-shadow: 6px 6px 7px var(--shadow);
  }
  .slide-welcome { left: 292px; top: 40px; width: 614px; height: 460px; }
  .slide-content { left: 122px; top: 536px; width: 476px; height: 357px; }
  .slide-thanks  { left: 657px; top: 530px; width: 477px; height: 357px; }

  .tiles {
    position: absolute;
    inset: 0;
    width: 100%;
    height: 100%;
  }
  .tile-pink  { fill: var(--pink); }
  .tile-cyan  { fill: var(--cyan); }
  .tile-mint  { fill: var(--mint); }
  .tile-stone { fill: var(--stone); }
  .tiles-faded { opacity: 0.18; }

  .brand {
    position: absolute;
    display: flex;
    align-items: flex-start;
    gap: 4px;
    font-family: "Arimo", Arial, sans-serif;
    font-weight: 700;
    color: var(--ink);
    line-height: 1.1;
  }
  .brand-mark {
    flex: none;
    background: var(--brand-red);
  }
  .slide-welcome .brand { left: 14px; top: 6px; font-size: 9px; }
  .slide-welcome .brand-mark { width: 18px; height: 18px; }
  .slide-content .brand,
  .slide-thanks .brand { left: 11px; top: 4px; font-size: 7px; }
  .slide-content .brand-mark,
  .slide-thanks .brand-mark { width: 14px; height: 14px; }

  .slide-heading {
    position: absolute;
    margin: 0;
    font-family: "Arimo", Arial, sans-serif;
    font-weight: 400;
    color: var(--ink);
    white-space: nowrap;
  }
  .slide-welcome .slide-heading { left: 261px; top: 243px; font-size: 29px; }
  .slide-thanks .slide-heading  { left: 203px; top: 187px; font-size: 23px; }

  .content-title {
    position: absolute;
    left: 165px;
    top: 55px;
    margin: 0;
    font-family: "Carlito", Calibri, sans-serif;
    font-weight: 400;
    font-size: 25px;
    color: var(--ink);
  }
  .task-list {
    position: absolute;
    left: 58px;
    top: 103px;
    margin: 0;
    padding: 0;
    list-style: none;
    font-family: "Arimo", Arial, sans-serif;
    font-size: 15.5px;
    color: var(--bullet-blue);
  }
  .task-list li {
    display: flex;
    align-items: center;
    gap: 6px;
    height: 24.7px;
  }
  .task-box {
    flex: none;
    width: 9px;
    height: 9px;
    border: 1.5px solid var(--bullet-blue);
    box-shadow: 1.5px 1.5px 0 var(--bullet-blue);
  }
</style>
</head>
<body>
<main class="board">

  <section class="slide slide-welcome" aria-label="Title slide">
    <svg class="tiles" viewBox="0 0 614 460" preserveAspectRatio="none" aria-hidden="true">
      <path class="tile-pink" d="M105,0 L403,0 L430,188 Q433,212 410,216 L162,249 Q140,252 137,230 Z"/>
      <path class="tile-cyan" d="M443,0 L614,0 L614,286 L465,286 Q443,286 443,264 Z"/>
      <path class="tile-mint" d="M145,460 L145,308 Q145,286 167,286 L421,286 Q443,286 443,308 L443,460 Z"/>
      <path class="tile-stone" d="M443,460 L443,308 Q443,286 465,286 L614,286 L614,460 Z"/>
    </svg>
    <div class="brand"><span class="brand-mark"></span><span>Fjordvik<br>Data Guild</span></div>
    <h1 class="slide-heading">WELCOME</h1>
  </section>

  <section class="slide slide-content" aria-label="Content slide">
    <svg class="tiles tiles-faded" viewBox="0 0 614 460" preserveAspectRatio="none" aria-hidden="true">
      <path class="tile-pink" d="M105,0 L403,0 L430,188 Q433,212 410,216 L162,249 Q140,252 137,230 Z"/>
      <path class="tile-cyan" d="M443,0 L614,0 L614,286 L465,286 Q443,286 443,264 Z"/>
      <path class="tile-mint" d="M145,460 L145,308 Q145,286 167,286 L421,286 Q443,286 443,308 L443,460 Z"/>
      <path class="tile-stone" d="M443,460 L443,308 Q443,286 465,286 L614,286 L614,460 Z"/>
    </svg>
    <div class="brand"><span class="brand-mark"></span><span>Fjordvik<br>Data Guild</span></div>
    <h2 class="content-title">Hva gjør vi?</h2>
    <ul class="task-list">
      <li><span class="task-box"></span>Markedsfører arrangementer</li>
      <li><span class="task-box"></span>Bidrar til å verve medlemmer</li>
      <li><span class="task-box"></span>Skaper synlighet i Sosiale Medier</li>
      <li><span class="task-box"></span>Bygger merkevare og FDGs omdømme</li>
    </ul>
  </section>

  <section class="slide slide-thanks" aria-label="Closing slide">
    <svg class="tiles" viewBox="0 0 614 460" preserveAspectRatio="none" aria-hidden="true">
      <path class="tile-pink" d="M105,0 L403,0 L430,188 Q433,212 410,216 L162,249 Q140,252 137,230 Z"/>
      <path class="tile-cyan" d="M443,0 L614,0 L614,286 L465,286 Q443,286 443,264 Z"/>
      <path class="tile-mint" d="M145,460 L145,308 Q145,286 167,286 L421,286 Q443,286 443,308 L443,460 Z"/>
      <path class="tile-stone" d="M443,460 L443,308 Q443,286 465,286 L614,286 L614,460 Z"/>
    </svg>
    <div class="brand"><span class="brand-mark"></span><span>Fjordvik<br>Data Guild</span></div>
    <h2 class="slide-heading">THANK YOU</h2>
  </section>

</main>
</body>
</html>
```